CGN Website (Cobalt Guard Networks)

We need a web design for an established company in Dubai, U.A.E, called Cobalt Guard Network. We provide a completed solutions in ICT-Information and Communication Technology (Computer, Networking, IP Telephony, Software and Hardware) and Security Systems (CCTV, Access Control, and System Integrator), our Services include Consultancy Planning and Design, Value Added Distribution, Implementation and Execution, Operations and Maintenance, Training and Development. We help our Clients to Develop and Secure their infrastructure. We would like to see design that use our logo theme, reflect our solutions and services, communicate to enterprise Technology and Security. Website must be responsive, Dynamic, symmetry or asymmetry or both.
Regards,

Target Market(s)

UAE

Industry/Entity Type

It Company

Coding

Coded - Design and coding required

Number of Pages Required

5+ page

Font styles to use
Sans Serif

Requirements
Must have
• Logo Theme, social media logos and links,
Nice to have
• Big blogs and banners
Should not have
• Many colors or congested design

```html
<!DOCTYPE html>
<html lang="en">
<head>
<meta charset="utf-8">
<title>Cobalt Guard Network</title>
<link href="https://fonts.googleapis.com/css2?family=Ubuntu:wght@400;500;700&display=swap" rel="stylesheet">
<style>
:root{
  --gold:#e6bd3c;
  --ink:#3f3f3f;
  --text:#6b6b6b;
  --muted:#9a9a9a;
  --line:#e2e2e2;
  --strip:#f4f4f4;
  --footer:#4b4b4b;
  --footer-dark:#3e3e3e;
  --white:#ffffff;
}
*{box-sizing:border-box;margin:0;padding:0}
html,body{width:1200px;height:2848px;overflow:hidden}
body{font-family:"Ubuntu",sans-serif;color:var(--text);background:var(--white);position:relative}
.abs{position:absolute}

/* header + hero */
.hero{left:0;top:0;width:1200px;height:580px;background:linear-gradient(135deg,#dfe6ec 0%,#b9c6d1 45%,#7f8f9c 100%)}
.topbar{left:0;top:0;width:1200px;height:80px;background:rgba(40,40,40,.78);display:flex;align-items:center;justify-content:space-between;padding:0 40px}
.brand{display:flex;align-items:center;gap:10px;color:var(--gold);font-size:20px;font-weight:500}
.brand-dot{width:26px;height:26px;border-radius:50%;background:var(--gold)}
.main-nav{display:flex;gap:42px;list-style:none}
.main-nav li{color:var(--white);font-size:16px}
.hero-title{left:0;top:360px;width:1200px;text-align:center;color:var(--white);font-size:50px;font-weight:500;letter-spacing:1px;text-shadow:0 2px 6px rgba(0,0,0,.25)}

/* services strip */
.services{left:0;top:580px;width:1200px;height:130px;background:var(--strip);display:flex;align-items:center;justify-content:center;gap:60px}
.svc-arrow{width:24px;height:24px;color:#b0b0b0}
.svc{display:flex;align-items:center;gap:12px;width:200px}
.svc-icon{width:42px;height:42px;border-radius:50%;background:#6d6d6d;flex:none;display:flex;align-items:center;justify-content:center}
.svc-icon span{width:14px;height:14px;border-radius:50%;background:var(--gold)}
.svc p{font-size:12px;line-height:16px;color:var(--text)}
.rule{left:40px;top:744px;width:1120px;height:1px;background:var(--line)}

/* headings */
.section-head{font-size:24px;font-weight:500;color:var(--ink);letter-spacing:.5px}
.side-head{display:flex;justify-content:space-between;align-items:center;width:300px;border-bottom:1px solid var(--line);padding-bottom:10px}
.pager{display:flex;gap:10px;color:var(--ink);font-size:16px}

/* blog */
.post-date{left:40px;width:72px;height:100px;background:var(--gold);color:var(--white);font-size:14px;font-weight:700;text-align:center;line-height:22px;padding-top:16px}
.share{left:40px;width:72px;display:flex;flex-direction:column;align-items:center;gap:9px}
.share small{font-size:13px;color:var(--muted)}
.share i{width:20px;height:20px;border-radius:50%;border:1.5px solid #8a8a8a;display:block}
.post-media{left:128px;width:620px}
.post-title{left:128px;width:620px;font-size:21px;font-weight:700;line-height:30px;color:var(--ink)}
.post-body{left:128px;width:620px;font-size:13px;line-height:20px;color:var(--muted)}
.btn{top:2648px;width:100px;height:36px;font-size:13px;font-weight:500;display:flex;align-items:center;justify-content:center;color:var(--ink)}
.btn-prev{left:128px;background:var(--gold);color:var(--white)}
.btn-next{left:248px;background:#dcdcdc}

/* sidebar */
.side{left:772px;width:300px}
.thumb{left:772px;width:300px}
.comment{left:772px;width:300px;display:flex;gap:16px}
.avatar{width:116px;height:128px;flex:none}
.comment-meta{padding-top:6px}
.comment-date{color:var(--gold);font-size:13px;font-weight:500}
.comment-name{color:var(--ink);font-size:13px;font-weight:500;margin:8px 0 6px}
.comment-text{font-size:12px;line-height:17px;color:var(--muted)}
.provide-group{left:772px;width:300px}
.provide-title{border-left:4px solid var(--gold);padding:6px 0 6px 12px;font-size:15px;color:var(--ink);line-height:22px;border-bottom:1px solid var(--line)}
.provide-list{list-style:none;padding:12px 0 0 16px}
.provide-list li{font-size:13px;line-height:26px;color:var(--muted)}

/* footer */
.footer{left:0;top:2700px;width:1200px;height:148px;background:var(--footer);text-align:center}
.social-row{display:flex;justify-content:center;gap:12px;padding-top:24px}
.social-row i{width:24px;height:24px;border-radius:50%;background:#6a6a6a;display:block}
.foot-nav{display:flex;justify-content:center;list-style:none;margin-top:18px}
.foot-nav li{color:var(--white);font-size:15px;padding:0 16px;border-right:1px solid #8a8a8a}
.foot-nav li:last-child{border-right:none}
.copyright{margin-top:16px;font-size:13px;color:#c8c8c8}
.to-top{right:16px;top:2808px;width:28px;height:28px;background:var(--footer-dark);color:var(--white);font-size:14px;display:flex;align-items:center;justify-content:center}
</style>
</head>
<body>

<section class="abs hero" role="img" aria-label="Photo of a person working at a laptop showing a bar chart report"></section>
<header class="abs topbar">
  <div class="brand"><span class="brand-dot"></span>Cobalt Guard</div>
  <ul class="main-nav">
    <li>Home</li><li>About Us</li><li>Services</li><li>Blog</li><li>News</li><li>FAQ's</li><li>Contact Us</li>
  </ul>
</header>
<h1 class="abs hero-title">COBALT GUARD NETWORK</h1>

<section class="abs services">
  <svg class="svc-arrow" viewBox="0 0 24 24"><path d="M15 5l-7 7 7 7" fill="none" stroke="currentColor" stroke-width="2"/></svg>
  <div class="svc"><div class="svc-icon"><span></span></div><p>Consultancy<br>Planning &amp; Design</p></div>
  <div class="svc"><div class="svc-icon"><span></span></div><p>Security System</p></div>
  <div class="svc"><div class="svc-icon"><span></span></div><p>Operations &amp;<br>Maintenance/Execution</p></div>
  <div class="svc"><div class="svc-icon"><span></span></div><p>Training and Development</p></div>
  <svg class="svc-arrow" viewBox="0 0 24 24"><path d="M9 5l7 7-7 7" fill="none" stroke="currentColor" stroke-width="2"/></svg>
</section>
<div class="abs rule"></div>

<!-- blog -->
<h2 class="abs section-head" style="left:128px;top:770px">BLOG</h2>

<div class="abs post-date" style="top:832px">JULY<br>15TH<br>2015</div>
<div class="abs share" style="top:950px"><small>Share</small><i></i><i></i><i></i><i></i><i></i><i></i><i></i></div>
<div class="abs post-media" style="top:832px;height:360px;background:linear-gradient(135deg,#0b2a55,#1d5fa8 55%,#0a1f3f)" role="img" aria-label="Hand touching a glowing network diagram of connected people icons"></div>
<h3 class="abs post-title" style="top:1208px">Lorem ipsum dolor sit amet, consectetur adipiscing elit, sed do eiusmod tempor incididunt ut labore et dolore magna aliqua.</h3>
<p class="abs post-body" style="top:1280px">Lorem ipsum dolor sit amet, consectetur adipiscing elit, sed do eiusmod tempor incididunt ut labore et dolore magna aliqua. Ut enim ad minim veniam, quis nostrud exercitation ullamco laboris nisi ut aliquip ex ea commodo consequat. Duis aute irure dolor in reprehenderit in voluptate velit esse cillum dolore eu fugiat nulla pariatur. Excepteur sint occaecat cupidatat non proident, sunt in culpa qui officia deserunt mollit anim id est laborum.</p>

<div class="abs post-date" style="top:1448px">JULY<br>15TH<br>2015</div>
<div class="abs share" style="top:1566px"><small>Share</small><i></i><i></i><i></i><i></i><i></i><i></i><i></i></div>
<div class="abs post-media" style="top:1448px;height:360px;background:linear-gradient(135deg,#2b3f66,#4a78b4 50%,#1d2b45)" role="img" aria-label="Screens showing several social media apps"></div>
<h3 class="abs post-title" style="top:1824px">Lorem ipsum dolor sit amet, consectetur adipiscing elit, sed do eiusmod tempor incididunt ut labore et dolore magna aliqua.</h3>
<p class="abs post-body" style="top:1900px">Lorem ipsum dolor sit amet, consectetur adipiscing elit, sed do eiusmod tempor incididunt ut labore et dolore magna aliqua. Ut enim ad minim veniam, quis nostrud exercitation ullamco laboris nisi ut aliquip ex ea commodo consequat. Duis aute irure dolor in reprehenderit in voluptate velit esse cillum dolore eu fugiat nulla pariatur. Excepteur sint occaecat cupidatat non proident, sunt in culpa qui officia deserunt mollit anim id est laborum.</p>

<div class="abs post-date" style="top:2068px">JULY<br>15TH<br>2015</div>
<div class="abs share" style="top:2186px"><small>Share</small><i></i><i></i><i></i><i></i><i></i><i></i><i></i></div>
<div class="abs post-media" style="top:2068px;height:352px;background:linear-gradient(135deg,#c9d6c9,#8fa6a0 50%,#d8c7a8)" role="img" aria-label="Hands holding a smartphone at a desk"></div>
<h3 class="abs post-title" style="top:2436px">Lorem ipsum dolor sit amet, consectetur adipiscing elit, sed do eiusmod tempor incididunt ut labore et dolore magna aliqua.</h3>
<p class="abs post-body" style="top:2512px">Lorem ipsum dolor sit amet, consectetur adipiscing elit, sed do eiusmod tempor incididunt ut labore et dolore magna aliqua. Ut enim ad minim veniam, quis nostrud exercitation ullamco laboris nisi ut aliquip ex ea commodo consequat. Duis aute irure dolor in reprehenderit in voluptate velit esse cillum dolore eu fugiat nulla pariatur. Excepteur sint occaecat cupidatat non proident, sunt in culpa qui officia deserunt mollit anim id est laborum.</p>

<div class="abs btn btn-prev">PREV</div>
<div class="abs btn btn-next">NEXT</div>

<!-- sidebar -->
<div class="abs side side-head" style="top:774px"><h2 class="section-head">RECENT POSTS</h2><div class="pager"><span>&#8249;</span><span>&#8250;</span></div></div>
<div class="abs thumb" style="top:832px;height:168px;background:linear-gradient(135deg,#1f4f86,#5f8fc6 60%,#203b5e)" role="img" aria-label="Security camera mounted on a wall"></div>
<div class="abs thumb" style="top:1012px;height:148px;background:linear-gradient(135deg,#0e2038,#2f5a8a 55%,#0b1626)" role="img" aria-label="Hand touching a digital security interface"></div>
<p class="abs side post-body" style="top:1172px;width:300px">Lorem ipsum dolor sit amet, consectetur adipiscing elit, sed do eiusmod tempor incididunt ut labore et dolore magna aliqua. Ut enim ad minim veniam.</p>

<div class="abs side side-head" style="top:1410px"><h2 class="section-head">COMMENTS</h2><div class="pager"><span>&#8249;</span><span>&#8250;</span></div></div>
<div class="abs comment" style="top:1464px">
  <div class="avatar" style="background:linear-gradient(135deg,#c8b7a2,#8c7b6a)" role="img" aria-label="Portrait photo of a commenter"></div>
  <div class="comment-meta"><div class="comment-date">JULY 15TH, 2015</div><div class="comment-name">Omar Keller</div><p class="comment-text">Great article on network security, very useful tips for our office setup.</p></div>
</div>
<div class="abs comment" style="top:1648px">
  <div class="avatar" style="background:linear-gradient(135deg,#b9b4ad,#6f6a64)" role="img" aria-label="Portrait photo of a commenter"></div>
  <div class="comment-meta"><div class="comment-date">JULY 15TH, 2015</div><div class="comment-name">Omar Keller</div><p class="comment-text">Thanks for sharing, the access control overview was clear and helpful.</p></div>
</div>
<div class="abs comment" style="top:1840px">
  <div class="avatar" style="background:linear-gradient(135deg,#d1c2ae,#8a7560)" role="img" aria-label="Portrait photo of a commenter"></div>
  <div class="comment-meta"><div class="comment-date">JULY 15TH, 2015</div><div class="comment-name">Omar Keller</div><p class="comment-text">Looking forward to more posts about CCTV planning and maintenance.</p></div>
</div>

<div class="abs side side-head" style="top:2066px"><h2 class="section-head">WHAT WE PROVIDE ?</h2></div>
<div class="abs provide-group" style="top:2140px">
  <div class="provide-title">ICT-Information and<br>Communication Technology</div>
  <ul class="provide-list"><li>Computer</li><li>Networking</li><li>IP Telephony</li><li>Software and Hardware</li></ul>
</div>
<div class="abs provide-group" style="top:2332px">
  <div class="provide-title">Security Systems</div>
  <ul class="provide-list"><li>CCTV</li><li>Access Control</li><li>System Integrator</li></ul>
</div>

<!-- footer -->
<footer class="abs footer">
  <div class="social-row"><i></i><i></i><i></i><i></i><i></i><i></i><i></i></div>
  <ul class="foot-nav"><li>Home</li><li>About Us</li><li>Services</li><li>Blog</li><li>News</li><li>FAQ's</li><li>Contact Us</li></ul>
  <p class="copyright">&copy; 2015 Company Name. All Rights Reserved</p>
</footer>
<div class="abs to-top">&#8963;</div>

</body>
</html>
```